Design for Certificate

Design a certificate for training, providing our company logo such as attachments. Company's name is "ØSTRA Velmark Advisory Ltd", please refer to our company profile: https://www.ostra-velmark.example/company_info

The style of the current certificate is also attached, and another certificate of another company can be referred to. Psd & jpg are required for the final draft (the layers of psd are not merged). Thanks!

```html
<!DOCTYPE html>
<html lang="en">
<head>
<meta charset="utf-8">
<title>ØSTRA Velmark Advisory Ltd – Certificate of Completion</title>
<link rel="stylesheet" href="https://fonts.googleapis.com/css2?family=Playfair+Display:wght@700&family=Montserrat:wght@400;500;600&display=swap">
<style>
  :root {
    --page-bg: #ececea;
    --frame-tan: #d7b597;
    --frame-dark: #2a2a2a;
    --paper: #f9f8f6;
    --pattern-line: #ead6c3;
    --accent-tan: #c39a78;
    --ink: #2b2b2b;
    --rule: #3a3a3a;
  }
  * { box-sizing: border-box; margin: 0; padding: 0; }
  html, body { width: 1200px; height: 1000px; overflow: hidden; }
  body {
    background: var(--page-bg);
    font-family: "Montserrat", Arial, sans-serif;
    color: var(--ink);
    position: relative;
  }
  .certificate {
    position: absolute;
    left: 100px; top: 146px;
    width: 1000px; height: 708px;
    background: var(--frame-tan);
    padding: 24px;
  }
  .certificate__inner {
    position: relative;
    width: 100%; height: 100%;
    border: 4px solid var(--frame-dark);
    overflow: hidden;
  }
  .certificate__pattern {
    position: absolute; inset: 0;
    background:
      radial-gradient(ellipse at 85% -20%, rgba(234,214,195,0.55), transparent 60%),
      radial-gradient(ellipse at 10% 110%, rgba(234,214,195,0.5), transparent 60%),
      var(--paper);
  }
  .certificate__content { position: absolute; inset: 0; }
  .title {
    position: absolute; left: 0; right: 0; top: 40px;
    text-align: center;
    font-family: "Playfair Display", Georgia, serif;
    font-weight: 700;
    font-size: 64px;
    line-height: 1.2;
    color: var(--accent-tan);
    letter-spacing: 1px;
  }
  .awarded {
    position: absolute; left: 0; right: 0; top: 138px;
    text-align: center;
    font-size: 28px;
    font-weight: 500;
    color: var(--accent-tan);
  }
  .rule {
    position: absolute;
    height: 1px;
    background: var(--rule);
  }
  .rule--recipient { left: 200px; width: 544px; top: 232px; }
  .completed {
    position: absolute; left: 0; right: 0; top: 250px;
    text-align: center;
    font-size: 17px;
  }
  .rule--course-top { left: 160px; width: 624px; top: 298px; }
  .course {
    position: absolute; left: 0; right: 0; top: 318px;
    text-align: center;
    font-size: 28px;
    font-weight: 500;
    white-space: nowrap;
  }
  .held {
    position: absolute; left: 150px; top: 404px;
    font-size: 20px;
  }
  .rule--date { left: 420px; width: 230px; top: 428px; }
  .rule--signature { left: 380px; width: 270px; top: 484px; }
  .signatory {
    position: absolute; left: 430px; top: 494px;
    font-size: 13px;
  }
  .brand {
    position: absolute; left: 690px; top: 420px;
    display: flex; align-items: center; gap: 12px;
  }
  .brand__mark {
    width: 16px; height: 16px; border-radius: 50%;
    background: var(--accent-tan);
  }
  .brand__name {
    font-family: "Montserrat", Arial, sans-serif;
    font-weight: 600;
    font-size: 50px;
    color: var(--accent-tan);
    letter-spacing: 2px;
  }
  .cert-number {
    position: absolute; left: 60px; top: 612px;
    font-size: 13px;
  }
  .rule--number { left: 178px; width: 220px; top: 626px; }
</style>
</head>
<body>
  <main class="certificate">
    <div class="certificate__inner">
      <div class="certificate__pattern" role="img" aria-label="Fine tan guilloche line pattern on white paper"></div>
      <div class="certificate__content">
        <h1 class="title">Certificate of Completion</h1>
        <p class="awarded">This certificate is awardet to</p>
        <div class="rule rule--recipient"></div>
        <p class="completed">has successfully completed</p>
        <div class="rule rule--course-top"></div>
        <p class="course">Brand reputation Management Training Course</p>
        <p class="held">Sixteen hours, held on</p>
        <div class="rule rule--date"></div>
        <div class="rule rule--signature"></div>
        <p class="signatory">Chief Technology Officer</p>
        <div class="brand">
          <span class="brand__mark"></span>
          <span class="brand__name">ØSTRA</span>
        </div>
        <p class="cert-number">Certificate No. :</p>
        <div class="rule rule--number"></div>
      </div>
    </div>
  </main>
</body>
</html>
```